Crestline Athletics and fitness is Hosting a Winter Renewal yoga class. World-renowned Rob Calloway will be teaching. Rob is a Life Empowerment Coach. This event will take place on January 5th, 2019 Time: 2pm - 4pmYoga at Optimum Sports and FitnessCost: $30 / $40 at the Door

Requirements
Must have
• Crestline Athletics and fitness Logo
• Crestline Lotus Yoga Logo

```html
<!DOCTYPE html>
<html lang="en">
<head>
<meta charset="utf-8">
<title>Crestline Athletics and Fitness – Winter Renewal Yoga Class</title>
<link href="https://fonts.googleapis.com/css2?family=Montserrat:wght@300;400&display=swap" rel="stylesheet">
<style>
  :root {
    --backdrop: #e6e6e6;
    --ink: #070707;
    --white: #ffffff;
    --ember-dark: #b3140c;
    --ember: #f0421a;
    --flame: #ff7a22;
    --glow: #ffd35a;
    --rule: #8a8a8a;
    --photo: #3a3a3a;
    --photo-light: #9a9a9a;
  }
  * { box-sizing: border-box; margin: 0; padding: 0; }
  html, body { width: 1200px; height: 986px; overflow: hidden; }
  body {
    background: var(--backdrop);
    font-family: "Montserrat", sans-serif;
    color: var(--white);
    position: relative;
  }
  .flyer {
    position: absolute;
    left: 250px; top: 40px;
    width: 700px; height: 906px;
    background: var(--ink);
    overflow: hidden;
  }
  .hero-art {
    position: absolute;
    left: 0; top: 0;
    width: 700px; height: 520px;
    background:
      radial-gradient(circle at 50% 52%, var(--glow) 0%, var(--flame) 22%, var(--ember) 50%, var(--ember-dark) 90%);
  }
  .hero-art::after {
    content: "";
    position: absolute;
    left: 0; right: 0; bottom: 0; height: 120px;
    background: linear-gradient(to bottom, rgba(7,7,7,0), var(--ink));
  }
  .brand {
    position: absolute;
    top: 46px; left: 0; right: 0;
    display: flex; align-items: center; justify-content: center;
    gap: 14px;
    z-index: 2;
  }
  .brand-dot {
    width: 64px; height: 64px;
    border-radius: 50%;
    background: var(--white);
  }
  .brand-name {
    font-weight: 400;
    color: var(--white);
    line-height: 1.1;
  }
  .brand-name .line-main { display: block; font-size: 34px; letter-spacing: 1px; text-transform: uppercase; }
  .brand-name .line-sub { display: block; font-size: 12px; letter-spacing: 4px; text-transform: uppercase; }
  .event-title {
    position: absolute;
    top: 556px; left: 30px;
    width: 550px;
    font-weight: 300;
    font-size: 34px;
    line-height: 1.2;
    letter-spacing: 0.5px;
    text-align: center;
    white-space: nowrap;
  }
  .instructor-photo {
    position: absolute;
    top: 536px; left: 594px;
    width: 80px; height: 80px;
    border: 1px solid var(--rule);
    background: radial-gradient(circle at 50% 40%, var(--photo-light), var(--photo) 70%);
  }
  .event-intro {
    position: absolute;
    top: 612px; left: 30px;
    width: 550px;
    font-weight: 300;
    font-size: 17px;
    line-height: 1.45;
    text-align: center;
  }
  .info-box {
    position: absolute;
    border: 1px dashed var(--rule);
    border-radius: 18px;
    font-weight: 300;
    font-size: 22px;
    line-height: 1.25;
    text-align: center;
    display: flex; align-items: center; justify-content: center;
  }
  .event-when { top: 730px; left: 60px; width: 260px; height: 90px; }
  .event-price { top: 690px; left: 450px; width: 200px; height: 84px; }
  .web-address {
    position: absolute;
    top: 838px; left: 0; right: 0;
    text-align: center;
    font-weight: 300;
    font-size: 22px;
    letter-spacing: 1px;
  }
</style>
</head>
<body>
  <main class="flyer">
    <div class="hero-art" role="img" aria-label="Silhouette of a yoga practitioner in a balancing pose before a glowing mandala and a dark pine tree skyline"></div>

    <header class="brand">
      <span class="brand-dot"></span>
      <span class="brand-name">
        <span class="line-main">Crestline</span>
        <span class="line-sub">Athletics and Fitness</span>
      </span>
    </header>

    <h1 class="event-title">Winter Renewal Yoga Class</h1>
    <div class="instructor-photo" role="img" aria-label="Portrait photo of instructor Rob Calloway"></div>

    <p class="event-intro">World-renowned Rob Calloway will be teaching.<br>Rob is a Life Empowerment Coach.</p>

    <div class="info-box event-when">January 5th, 2019<br>2pm - 4pm</div>
    <div class="info-box event-price">$30/$40<br>at the Door</div>

    <p class="web-address">www.crestlineaf.com</p>
  </main>
</body>
</html>
```